2018 Vision Board Workshop

I need to promote this workshop on both an 8.5x11 sheet and a 5x7 card. I do have a logo that needs to be present. I'd like to stay true to my branded colors. The flyer needs to project the excitement of a new year and the possibilities of what a person can create, produce, explore in their lives by putting it all on a vision board. Creating the vision of what you want will inspire you to achieve your goals and dreams. Looking at your vision board each day will propel you into taking action as you chart your course to achieve what you truly want.
The flyer needs to have the following information:
The workshop date and time - Sat., Jan. 13, 2018, 10:30-1:30
The location is - Lantern Hall 7B, 2648 Maple Ridge Dr, Colorado Springs, Co 80920
in the FORGE Room
My name and contact information - Laura Pendleton
Text and voice 303-555-0147
Email - laura@joy-grows-daily.example
Website - joy-grows-daily.example
The fee is $45. All materials are provided.

My company is called Joy Grows Daily. I am a Life Coach, author, speaker and workshop leader.\ I wrote this program, Joy Grows Daily to teach concepts and supporting skills for living with more happiness, satisfaction and fulfillment. Thanks for reading this!! Laura

Target Market(s)

Primarily women, educated, motivated, proactive in their own lives and well being

Font styles to use
Other font styles liked:
• I have been using Century Gothic. I'm open to new ideas.

Requirements
Must have
• The Joy Grows Daily logo
• The flyer needs to have the following information:
• The workshop date and time - Sat., Jan. 13, 2018, 10:30-1:30
• The location is - Lantern Hall 7B, 2648 Maple Ridge Dr, Colorado Springs, Co 80920
• in the FORGE Room
• My name and contact information - Laura Pendleton
• Text and voice 303-555-0147
• Email - laura@joy-grows-daily.example
• Website - joy-grows-daily.example
• The fee is $45. All materials are provided.
Nice to have
• The Joy Grows Daily branded colors in the design
• Images of vision boards

```html
<!DOCTYPE html>
<html lang="en">
<head>
<meta charset="utf-8">
<title>2018 Vision Board Workshop</title>
<link rel="stylesheet" href="https://fonts.googleapis.com/css2?family=Montserrat:wght@600;700&family=Questrial&display=swap">
<style>
:root{
  --blue:#3a9fdb;
  --green:#8cc63f;
  --cork:#c8a678;
  --cork-dark:#b8946a;
  --paper:#ffffff;
  --ink:#2a2a2a;
  --stage:#eceef0;
  --tape-blue:#7cc0ea;
  --tape-green:#b3dc7c;
}
*{box-sizing:border-box;margin:0;padding:0}
html,body{width:1200px;height:854px;overflow:hidden}
body{background:var(--stage);position:relative;font-family:"Questrial",sans-serif;color:var(--ink)}
.piece{position:absolute;overflow:hidden;background:var(--paper);box-shadow:0 4px 14px rgba(0,0,0,.18)}
.cork{position:absolute;background:linear-gradient(160deg,var(--cork) 0%,var(--cork-dark) 100%)}
.note{position:absolute;background:var(--paper);display:flex;align-items:center;justify-content:center;box-shadow:0 2px 4px rgba(0,0,0,.25);font-family:"Questrial",sans-serif;white-space:nowrap}
.note.blue-text{color:var(--blue)}
.note.green-text{color:var(--green)}
.note::before{content:"";position:absolute;top:-6px;left:30%;width:36px;height:10px;background:var(--tape-blue);opacity:.85}
.note.green-tape::before{background:var(--tape-green)}
.headline{font-family:"Montserrat",sans-serif;font-weight:700;letter-spacing:.5px;white-space:nowrap}
.strip{position:absolute;background:var(--paper);display:flex;align-items:center;justify-content:center;box-shadow:0 2px 4px rgba(0,0,0,.2)}
.year{color:var(--blue)}
.year-paper{border-bottom:2px dashed #ddd}
.vision{color:var(--green)}
.workshop{color:var(--blue)}
.host-band{position:absolute;background:var(--blue);color:#fff;display:flex;align-items:center;justify-content:center;font-family:"Montserrat",sans-serif;font-weight:600;white-space:nowrap}
.photo{position:absolute;border:4px solid #fff;box-shadow:0 2px 5px rgba(0,0,0,.3)}
.photo-woman{background:linear-gradient(180deg,#a7c6d8 0%,#5f8ea9 100%)}
.photo-pier{background:linear-gradient(180deg,#6b5544 0%,#a8763f 100%)}
.photo-stairs{background:linear-gradient(180deg,#d6dde3 0%,#a9c196 100%)}
.date-tab{position:absolute;background:var(--blue);color:#fff;display:flex;align-items:center;justify-content:center;white-space:nowrap;clip-path:polygon(2% 0,100% 0,98% 100%,0 100%)}
.info-box{position:absolute;background:var(--green);color:#fff;line-height:1.22}
.info-box b{font-weight:700;font-family:"Montserrat",sans-serif}
.fee{position:absolute;background:#fff;border:3px solid var(--green);border-radius:50%;display:flex;flex-direction:column;align-items:center;justify-content:center;color:var(--blue);font-family:"Montserrat",sans-serif;font-weight:600;line-height:1.15}
.brand{position:absolute;display:flex;align-items:center;gap:8px;color:var(--green);white-space:nowrap}
.brand-dot{border-radius:50%;background:var(--blue);flex:none}
.headshot{position:absolute;border-radius:50%;border:4px solid var(--blue);background:linear-gradient(180deg,#e2c49c 0%,#b99466 100%)}
.name-band{position:absolute;background:var(--blue);color:#fff;display:flex;align-items:center;padding-left:12px;white-space:nowrap}
.roles{position:absolute;color:var(--green);line-height:1.25}
.contact{position:absolute;color:var(--blue);line-height:1.4}
.contact-band{position:absolute;left:0;background:var(--blue);color:#fff;display:flex;align-items:center;justify-content:flex-end;padding-right:6px;white-space:nowrap;clip-path:polygon(0 0,100% 0,98% 100%,0 100%)}
.footer-bar{position:absolute;left:0;bottom:0;width:100%;display:flex;color:#fff}
.footer-web{background:var(--blue);display:flex;align-items:center;justify-content:center;font-family:"Montserrat",sans-serif;font-weight:600}
.footer-note{background:var(--green);flex:1;display:flex;align-items:center;justify-content:center}
.supplies{position:absolute;background:linear-gradient(180deg,rgba(255,255,255,0) 0%,#eef1f3 35%,#e4e8eb 100%)}
.materials{position:absolute;color:var(--blue);white-space:nowrap}
</style>
</head>
<body>

<section class="piece flyer-letter" style="left:72px;top:58px;width:534px;height:692px">
  <div class="cork" style="left:0;top:0;width:534px;height:386px"></div>

  <div class="note green-text green-tape" style="left:32px;top:26px;width:106px;height:44px;transform:rotate(3deg);font-size:26px">DREAMS</div>
  <div class="strip year-paper" style="left:168px;top:32px;width:212px;height:66px"><span class="headline year" style="font-size:52px">2018</span></div>
  <div class="note blue-text" style="left:412px;top:30px;width:90px;height:38px;transform:rotate(4deg);font-size:22px">GOALS</div>
  <div class="strip" style="left:88px;top:98px;width:368px;height:50px"><span class="headline vision" style="font-size:42px">VISION BOARD</span></div>
  <div class="note blue-text green-tape" style="left:32px;top:162px;width:86px;height:44px;transform:rotate(-8deg);font-size:28px">Feel</div>
  <div class="strip" style="left:124px;top:152px;width:284px;height:50px"><span class="headline workshop" style="font-size:42px">WORKSHOP</span></div>
  <div class="note blue-text green-tape" style="left:438px;top:158px;width:80px;height:44px;transform:rotate(8deg);font-size:26px">Create</div>

  <div class="photo photo-woman" role="img" aria-label="Photo of a joyful woman with raised arms by the sea" style="left:4px;top:210px;width:178px;height:154px;transform:rotate(-2deg)"></div>
  <div class="photo photo-pier" role="img" aria-label="Photo of a wooden pier at sunset" style="left:190px;top:214px;width:166px;height:148px"></div>
  <div class="photo photo-stairs" role="img" aria-label="Photo of a spiral staircase around a green garden" style="left:356px;top:206px;width:176px;height:156px;transform:rotate(2deg)"></div>
  <div class="host-band" style="left:268px;top:200px;width:138px;height:40px;transform:rotate(-6deg);font-size:22px">with Laura</div>

  <div class="note green-text green-tape" style="left:80px;top:338px;width:80px;height:36px;transform:rotate(-4deg);font-size:26px">Joy</div>
  <div class="note green-text green-tape" style="left:238px;top:346px;width:92px;height:36px;font-size:24px">Explore</div>
  <div class="note green-text green-tape" style="left:432px;top:342px;width:88px;height:40px;transform:rotate(-6deg);font-size:26px">Climb</div>

  <div class="brand" style="left:40px;top:442px;font-size:22px"><span class="brand-dot" style="width:18px;height:18px"></span>Joy Grows Daily</div>

  <div class="headshot" role="img" aria-label="Portrait of Laura Pendleton" style="left:10px;top:488px;width:104px;height:104px"></div>
  <div class="name-band" style="left:114px;top:496px;width:142px;height:26px;font-size:17px">Laura Pendleton</div>
  <div class="roles" style="left:124px;top:534px;font-size:15px">Author, Coach,<br>Speaker and<br>Workshop Leader</div>
  <div class="contact" style="left:32px;top:614px;font-size:14.5px">Text and voice 303-555-0147<br>Email - laura@joy-grows-daily.example</div>

  <div class="info-box" style="left:274px;top:434px;width:242px;height:182px;padding:8px 14px;font-size:16px">
    <p><b>Time:</b> 10:30-1:30</p>
    <p style="margin-top:12px"><b>Location:</b> Lantern Hall 7B,<br>2648 Maple Ridge Dr,<br>Colorado Springs, Co 80920<br>in the FORGE Room</p>
  </div>
  <div class="date-tab" style="left:250px;top:402px;width:278px;height:32px;font-size:21px">Date : Sat., Jan. 13. 2018</div>
  <div class="fee" style="left:324px;top:562px;width:192px;height:88px;transform:rotate(-8deg);font-size:19px"><span>Registration</span><span>Fee: $45</span></div>

  <div class="footer-bar" style="height:31px">
    <div class="footer-web" style="width:270px;font-size:15px">joy-grows-daily.example</div>
    <div class="footer-note" style="font-size:14px">All materials are provided</div>
  </div>
</section>

<section class="piece card-front" style="left:637px;top:54px;width:482px;height:342px">
  <div class="cork" style="left:0;top:0;width:482px;height:342px"></div>
  <div class="photo photo-stairs" role="img" aria-label="Photo of a spiral staircase around a green garden" style="left:3px;top:2px;width:164px;height:148px;transform:rotate(-3deg)"></div>
  <div class="strip year-paper" style="left:171px;top:17px;width:188px;height:58px"><span class="headline year" style="font-size:46px">2018</span></div>
  <div class="note blue-text" style="left:367px;top:34px;width:98px;height:40px;transform:rotate(2deg);font-size:22px">GOALS</div>
  <div class="strip" style="left:175px;top:82px;width:282px;height:38px"><span class="headline vision" style="font-size:31px">VISION BOARD</span></div>
  <div class="strip" style="left:203px;top:124px;width:220px;height:37px"><span class="headline workshop" style="font-size:31px">WORKSHOP</span></div>
  <div class="note green-text green-tape" style="left:47px;top:126px;width:92px;height:34px;transform:rotate(-5deg);font-size:22px">Climb</div>
  <div class="photo photo-woman" role="img" aria-label="Photo of a joyful woman with raised arms by the sea" style="left:74px;top:163px;width:170px;height:140px"></div>
  <div class="note blue-text" style="left:10px;top:182px;width:94px;height:32px;font-size:20px;color:#8fb6cf">DREAMS</div>
  <div class="host-band" style="left:311px;top:153px;width:146px;height:44px;transform:rotate(-6deg);font-size:22px">with Laura</div>
  <div class="date-tab" style="left:227px;top:206px;width:204px;height:24px;background:var(--green);font-size:15px">Date : Sat., Jan. 13. 2018</div>
  <div class="info-box" style="left:243px;top:230px;width:192px;height:90px;background:var(--blue);transform:rotate(-1deg);padding:6px 8px 6px 28px;font-size:11px">
    <p>Time:&nbsp; 10:30-1:30</p>
    <p><b>Location:</b> Lantern Hall 7B,<br>2648 Maple Ridge Dr,<br>Colorado Springs, Co 80920<br>in the FORGE Room</p>
  </div>
  <div class="note green-text green-tape" style="left:27px;top:258px;width:92px;height:40px;font-size:26px">Joy</div>
  <div class="note green-text green-tape" style="left:141px;top:282px;width:102px;height:40px;font-size:24px">Explore</div>
</section>

<section class="piece card-back" style="left:693px;top:429px;width:480px;height:343px">
  <div class="supplies" role="img" aria-label="Photo of desk supplies: marker, paper clips and sticky notes" style="left:0;top:230px;width:480px;height:113px"></div>

  <div class="brand" style="left:30px;top:44px;font-size:23px"><span class="brand-dot" style="width:18px;height:18px"></span>Joy Grows Daily</div>

  <div class="headshot" role="img" aria-label="Portrait of Laura Pendleton" style="left:19px;top:111px;width:72px;height:72px;border-width:3px"></div>
  <div class="name-band" style="left:95px;top:122px;width:138px;height:22px;font-size:15px">Laura Pendleton</div>
  <div class="roles" style="left:107px;top:148px;font-size:11.5px">Author, Coach, Speaker<br>and Workshop Leader</div>

  <div class="contact-band" style="top:202px;width:239px;height:15px;font-size:10.5px">Text and voice 303-555-0147</div>
  <div class="contact-band" style="top:229px;width:239px;height:15px;font-size:10.5px">Email - laura@joy-grows-daily.example</div>
  <div class="contact-band" style="top:258px;width:239px;height:15px;font-size:10.5px">Website - joy-grows-daily.example</div>

  <div class="info-box" style="left:261px;top:53px;width:189px;height:160px;padding:10px 10px;font-size:13px">
    <p><b>Time:</b> 10:30-1:30</p>
    <p style="margin-top:4px"><b>Location:</b> Lantern Hall 7B,<br>2648 Maple Ridge Dr,<br>Colorado Springs,<br>Co 80920<br>in the FORGE Room</p>
  </div>
  <div class="date-tab" style="left:243px;top:27px;width:216px;height:26px;font-size:16px">Date : Sat., Jan. 13. 2018</div>
  <div class="fee" style="left:277px;top:181px;width:150px;height:74px;transform:rotate(-7deg);font-size:15px"><span>Registration</span><span>Fee: $45</span></div>
  <div class="materials" style="left:275px;top:300px;font-size:14px">All materials are provided</div>
</section>

</body>
</html>
```